Template for a Holiday Look Book

We need a holiday lookbook that we can use at a few different golf and country clubs. I am hoping we can get a design nailed down, that they would then be able to tweak and alter from club to club. We have Marketing Directors at each Club, but no one has the time to make this from scratch, but could tweak it much easier once the template is created. I have attached a word document with ideas and have a google file we have started for pictures as well.

Target Market(s)

counrty club members

Industry/Entity Type

Country Club

Font styles to use
Sans Serif

Colors
0355a3
ffffff
eaf1f7

Requirements
Must have
• holiday look and feel....enticing the items that would be purchased

```html
<!DOCTYPE html>
<html lang="en">
<head>
<meta charset="utf-8">
<title>Holiday Look Book – Briar Ridge</title>
<link rel="stylesheet" href="https://fonts.googleapis.com/css2?family=Fira+Sans:wght@400;500;600&display=swap">
<style>
  :root {
    --club-blue: #0d3f7f;
    --brand-blue: #0355a3;
    --pale-blue: #eaf1f7;
    --gold: #a58b3d;
    --white: #ffffff;
    --backdrop: #d9dcdf;
    --ink-light: #e6edf6;
  }
  * { box-sizing: border-box; margin: 0; padding: 0; }
  html, body { width: 1200px; height: 800px; overflow: hidden; }
  body {
    background: var(--backdrop);
    font-family: "Fira Sans", Arial, sans-serif;
    color: var(--white);
  }
  .spread {
    position: absolute; left: 50px; top: 40px;
    width: 1100px; height: 720px;
    display: flex;
    box-shadow: 0 6px 24px rgba(0,0,0,.18);
  }
  .page { position: relative; width: 550px; height: 720px; background: var(--white); overflow: hidden; }
  .page--left { border-right: 1px solid #e2e4e7; }

  .offer-card { position: absolute; left: 50px; width: 400px; }
  .offer-card--tennis { top: 50px; }
  .offer-card--fitness { top: 300px; }
  .photo { display: block; width: 100%; }
  .photo--tennis { height: 150px; background: linear-gradient(180deg, #3d5a3a 0%, #2f5f8f 45%, #2a558a 100%); }
  .photo--fitness { height: 150px; background: linear-gradient(160deg, #8fa382 0%, #6d7f63 55%, #3b3f3c 100%); }
  .offer-body {
    background: var(--club-blue);
    padding: 9px 16px 14px;
    text-align: center;
    font-size: 11px; line-height: 1.32; color: var(--ink-light);
  }
  .offer-title { font-weight: 600; font-size: 12.5px; color: var(--white); margin-bottom: 2px; }
  .offer-body p + .offer-title { margin-top: 9px; }

  .photo--banquet {
    position: absolute; left: 0; top: 0; width: 550px; height: 300px;
    background: linear-gradient(180deg, #3a3f9a 0%, #6b62b0 40%, #b9a98a 75%, #d8c79e 100%);
  }
  .menu-panel {
    position: absolute; border-radius: 14px;
    font-size: 12px; line-height: 1.3;
  }
  .menu-panel--food {
    left: 95px; top: 275px; width: 190px;
    background: var(--club-blue); padding: 48px 14px 20px 16px;
    color: var(--ink-light); font-weight: 500;
  }
  .menu-tab {
    position: absolute; left: 0; top: 0; width: 100%; height: 36px;
    background: var(--gold); border-radius: 14px 14px 0 0;
    font-size: 15px; font-weight: 500; color: var(--white);
    padding: 8px 16px;
  }
  .menu-panel--food p { margin-bottom: 12px; }
  .menu-panel--food p:last-child { margin-bottom: 0; }
  .menu-panel--food .lead { font-size: 10.5px; font-weight: 400; line-height: 1.28; margin-bottom: 6px; }
  .menu-panel--family {
    left: 305px; top: 250px; width: 195px; height: 380px;
    background: var(--gold); padding: 18px 18px;
    font-size: 14px; color: var(--white);
  }
  .menu-panel--family ul { list-style: none; }
  .menu-panel--family li { margin-bottom: 14px; }
  .menu-panel--family .panel-heading { margin-bottom: 16px; line-height: 1.25; }
</style>
</head>
<body>
<main class="spread">
  <section class="page page--left">
    <article class="offer-card offer-card--tennis">
      <div class="photo photo--tennis" role="img" aria-label="Players on outdoor tennis courts"></div>
      <div class="offer-body">
        <p class="offer-title">Tennis Skills Lessons (4 pack) - $280</p>
        <p>T-Fit – Off court training for on court success! Learn the latest fitness training techniques with our fitness profession that will take your tennis game to a new level. 2 – 1 hr. sessions $150</p>
      </div>
    </article>

    <article class="offer-card offer-card--fitness">
      <div class="photo photo--fitness" role="img" aria-label="Members training on cardio machines in the fitness center"></div>
      <div class="offer-body">
        <p class="offer-title">Golf Fit Lessons $165 - Get Lucky! $40</p>
        <p>Get two-for-1 entry during our Lucky Clover 5K. Bring a partner and receive 2 entries for the price of 1 for our most-popular run, the Lucky Clover 5k. After the run, enjoy a cold drink of the Irish to celebrate.</p>
        <p class="offer-title">Shop for Health</p>
        <p>Experience a trip to the grocery store with our Nutritional Specialist, who will teach you how to prepare a healthy meal option. They will show you how to determine the perfect healthy ingredients.</p>
        <p class="offer-title">Muscle Massage</p>
        <p>Beach season is right around the corner, get ready with personalized training with our Fitness Director, Sam Whitlow. He will show you the proper techniques and help you set and achieve your goals!</p>
      </div>
    </article>
  </section>

  <section class="page page--right">
    <div class="photo--banquet" role="img" aria-label="Banquet room set with round tables, gold chargers and purple lighting"></div>

    <div class="menu-panel menu-panel--food">
      <h2 class="menu-tab">Food &amp; Beverage</h2>
      <p class="lead">Tasting Room Dinners for 8<br>Be a VIP, grab 7 of your closest friends, and experience a unique dining experience in our BRAND-NEW Briar Ridge Tasting Room! This 5-course meal, which will be tailored to fit your requested theme, will be one of the first opportunities to experience the new Clubhouse at Briar Ridge.</p>
      <p>Cookie Cheer $xx</p>
      <p>A private chef’s dinner party</p>
      <p>Briar Ridge Mug Club</p>
      <p>Custom cooking class<br>for 4 with Chef Marco</p>
      <p>Wine or Beer of the Month Club</p>
    </div>

    <div class="menu-panel menu-panel--family">
      <p class="panel-heading">For the BUSY PARENTS<br>Spread for this</p>
      <ul>
        <li>Santa stuff?</li>
        <li>Stocking Stuffers – what can this be?</li>
        <li>Birthday party</li>
        <li>Kid’s Corner hours</li>
        <li>Spa packages</li>
        <li>Camp packages</li>
        <li>Take Out/Mobile Food Ordering Vouchers</li>
      </ul>
    </div>
  </section>
</main>
</body>
</html>
```